Package design for Mica powder sachets

Our mica powder product comes in two sets of colors, a set of 60 and 35 packed inside sachet bags individually. This project will require two sizes of the packing box , one for the set of 60 and other for 35. We do not have a specific design requirement as long as the design reflects the theme of our product. Box diagram for both sizes is attached together with color chart, content, logo, sachet design and sample of a packaging design we like. The content is the same for both sizes accept for number of colors included.

```html
<!DOCTYPE html>
<html lang="en">
<head>
<meta charset="utf-8">
<title>Lumen Crafts – 60 Mica Powder Colors Box Dieline</title>
<link rel="stylesheet" href="https://fonts.googleapis.com/css2?family=Questrial&family=Arimo&display=swap">
<style>
  :root {
    --paper: #ffffff;
    --ink: #000000;
    --dieline: #9a9a9a;
    --note-orange: #f7931e;
    --tagline: #b5d334;
    --accent-orange: #f2a01f;
    --accent-pink: #e8348f;
    --band-blue: #4f9be0;
    --badge-violet: #b57cd8;
    --brand-dark: #1d1d1d;
    --white: #ffffff;
  }
  html, body { margin: 0; padding: 0; overflow: hidden; background: var(--paper); }
  .dieline-sheet { position: relative; width: 1189px; height: 1200px; overflow: hidden; background: var(--paper); }
  .dieline-art { position: absolute; inset: 0; display: block; }
  .panel-label { position: absolute; left: 295px; width: 601px; text-align: center; font-family: "Arimo", sans-serif; }
  .back-title { top: 208px; font-size: 52px; color: var(--white); }
  .back-note { top: 303px; font-size: 29px; line-height: 34px; color: var(--note-orange); }

  .art-text { font-family: "Questrial", sans-serif; }
  .count-text { fill: var(--white); font-family: "Questrial", sans-serif; }
  .words-text { fill: var(--white); font-family: "Questrial", sans-serif; }
  .brand-text { fill: var(--brand-dark); font-family: "Questrial", sans-serif; letter-spacing: 3px; }
  .brand-text.on-dark { fill: var(--white); letter-spacing: 5px; }
  .tagline-text { fill: var(--tagline); font-family: "Questrial", sans-serif; font-size: 9.6px; }
  .badge-count { fill: var(--accent-orange); font-family: "Questrial", sans-serif; font-size: 40px; }
  .badge-line { fill: var(--white); font-family: "Questrial", sans-serif; font-size: 13.5px; }
  .badge-colors { fill: var(--badge-violet); font-family: "Questrial", sans-serif; font-size: 12px; }
  .band-text { fill: var(--white); font-family: "Arimo", sans-serif; font-size: 9.5px; }
</style>
</head>
<body>
<main class="dieline-sheet">
  <svg class="dieline-art" viewBox="0 0 1189 1200" width="1189" height="1200">
    <defs>
      <radialGradient id="powder-burst" cx="50%" cy="50%" r="50%">
        <stop offset="0" stop-color="#f4e9f2"/>
        <stop offset="0.25" stop-color="#f25aa8"/>
        <stop offset="0.5" stop-color="#f6c21c"/>
        <stop offset="0.72" stop-color="#3aa0e0"/>
        <stop offset="0.9" stop-color="#6a2fa0" stop-opacity="0.5"/>
        <stop offset="1" stop-color="#000" stop-opacity="0"/>
      </radialGradient>
      <linearGradient id="wood-grain" x1="0" y1="0" x2="1" y2="0">
        <stop offset="0" stop-color="#2a1a10"/>
        <stop offset="0.5" stop-color="#5a3a22"/>
        <stop offset="1" stop-color="#4a2e1a"/>
      </linearGradient>
      <linearGradient id="badge-rim" x1="0" y1="0" x2="1" y2="1">
        <stop offset="0" stop-color="#f2a01f"/>
        <stop offset="0.5" stop-color="#b57cd8"/>
        <stop offset="1" stop-color="#e8348f"/>
      </linearGradient>
      <linearGradient id="band-fill" x1="0" y1="0" x2="1" y2="0">
        <stop offset="0" stop-color="#4f9be0"/>
        <stop offset="0.55" stop-color="#9b6fd0"/>
        <stop offset="1" stop-color="#e8348f"/>
      </linearGradient>
      <radialGradient id="jar-tones" cx="50%" cy="50%" r="50%">
        <stop offset="0" stop-color="#b9643a"/>
        <stop offset="0.7" stop-color="#7d4a32"/>
        <stop offset="1" stop-color="#3a2a22"/>
      </radialGradient>
      <clipPath id="clip-top-strip"><rect x="295" y="533" width="601" height="133"/></clipPath>
      <clipPath id="clip-bottom-strip"><rect x="295" y="1066" width="601" height="133"/></clipPath>
      <clipPath id="clip-left-side"><rect x="148" y="666" width="148" height="400"/></clipPath>
      <clipPath id="clip-right-side"><rect x="896" y="666" width="145" height="400"/></clipPath>
      <clipPath id="clip-front"><rect x="295" y="666" width="601" height="400"/></clipPath>
    </defs>

    <!-- box structure -->
    <g class="dieline" fill="var(--ink)" stroke="var(--dieline)" stroke-width="0.8">
      <rect x="295" y="2" width="601" height="132"/>
      <path d="M295 2 H240 C185 2 150 60 148 115 Q148 134 168 134 H295 Z"/>
      <path d="M896 2 H951 C1006 2 1041 60 1043 115 Q1043 134 1023 134 H896 Z"/>
      <rect x="295" y="134" width="601" height="399"/>
      <path d="M295 134 L180 173 Q148 185 148 215 V455 Q148 480 180 492 L295 533 Z"/>
      <path d="M896 134 L1011 173 Q1043 185 1043 215 V455 Q1043 480 1011 492 L896 533 Z"/>
      <rect x="148" y="534" width="147" height="124"/>
      <rect x="896" y="534" width="145" height="124"/>
      <rect x="295" y="533" width="601" height="133"/>
      <rect x="1" y="666" width="147" height="400"/>
      <rect x="148" y="666" width="148" height="400"/>
      <rect x="295" y="666" width="601" height="400"/>
      <rect x="896" y="666" width="145" height="400"/>
      <rect x="1041" y="666" width="147" height="400"/>
      <rect x="148" y="1074" width="147" height="125"/>
      <rect x="896" y="1074" width="145" height="125"/>
      <rect x="295" y="1066" width="601" height="133"/>
    </g>

    <!-- top strip (inverted) -->
    <g clip-path="url(#clip-top-strip)">
      <ellipse cx="700" cy="600" rx="220" ry="95" fill="url(#powder-burst)" role="img" aria-label="Photograph of a colourful powder explosion"/>
      <path d="M295 533 H440 Q485 600 440 666 H295 Z" fill="var(--white)"/>
      <path d="M440 533 Q485 600 440 666" fill="none" stroke="var(--accent-orange)" stroke-width="5"/>
    </g>
    <g transform="translate(385 598) rotate(180)">
      <text class="brand-text" x="0" y="-4" font-size="20" text-anchor="middle">Lumen</text>
      <text class="brand-text" x="0" y="20" font-size="20" text-anchor="middle">Crafts</text>
    </g>
    <g transform="translate(682 597) rotate(180)">
      <text class="count-text" x="-84" y="13" font-size="36">60</text>
      <text class="words-text" x="-36" y="3" font-size="15">MICA POWDER</text>
      <text class="words-text" x="-36" y="15" font-size="11">COLORS</text>
    </g>

    <!-- bottom strip -->
    <g clip-path="url(#clip-bottom-strip)">
      <ellipse cx="560" cy="1135" rx="210" ry="95" fill="url(#powder-burst)" role="img" aria-label="Photograph of a colourful powder explosion"/>
      <path d="M896 1066 H752 Q707 1133 752 1199 H896 Z" fill="var(--white)"/>
      <path d="M752 1066 Q707 1133 752 1199" fill="none" stroke="var(--accent-orange)" stroke-width="5"/>
    </g>
    <text class="brand-text" x="815" y="1130" font-size="20" text-anchor="middle">Lumen</text>
    <text class="brand-text" x="815" y="1155" font-size="20" text-anchor="middle">Crafts</text>
    <g transform="translate(507 1138)">
      <text class="count-text" x="-84" y="13" font-size="36">60</text>
      <text class="words-text" x="-36" y="3" font-size="15">MICA POWDER</text>
      <text class="words-text" x="-36" y="15" font-size="11">COLORS</text>
    </g>

    <!-- left side panel -->
    <g clip-path="url(#clip-left-side)">
      <rect x="148" y="666" width="148" height="400" fill="url(#wood-grain)" role="img" aria-label="Dark wood texture"/>
      <ellipse cx="221" cy="760" rx="140" ry="150" fill="url(#powder-burst)" role="img" aria-label="Photograph of a colourful powder explosion"/>
      <path d="M148 930 Q221 890 296 930 V1066 H148 Z" fill="var(--white)"/>
      <path d="M148 930 Q221 890 296 930" fill="none" stroke="var(--accent-orange)" stroke-width="5"/>
    </g>
    <g transform="translate(221 749) rotate(90)">
      <text class="count-text" x="-62" y="12" font-size="30">60</text>
      <text class="words-text" x="-24" y="2" font-size="12.5">MICA POWDER</text>
      <text class="words-text" x="-24" y="13" font-size="9.5">COLORS</text>
    </g>
    <g transform="translate(218 990) rotate(90)">
      <text class="brand-text" x="0" y="-4" font-size="20" text-anchor="middle">Lumen</text>
      <text class="brand-text" x="0" y="20" font-size="20" text-anchor="middle">Crafts</text>
    </g>

    <!-- right side panel -->
    <g clip-path="url(#clip-right-side)">
      <rect x="896" y="666" width="145" height="400" fill="url(#wood-grain)" role="img" aria-label="Dark wood texture"/>
      <ellipse cx="975" cy="985" rx="140" ry="155" fill="url(#powder-burst)" role="img" aria-label="Photograph of a colourful powder explosion"/>
      <path d="M896 666 H1041 V800 Q968 842 896 800 Z" fill="var(--white)"/>
      <path d="M896 800 Q968 842 1041 800" fill="none" stroke="var(--accent-orange)" stroke-width="5"/>
    </g>
    <g transform="translate(973 748) rotate(-90)">
      <text class="brand-text" x="0" y="-4" font-size="20" text-anchor="middle">Lumen</text>
      <text class="brand-text" x="0" y="20" font-size="20" text-anchor="middle">Crafts</text>
    </g>
    <g transform="translate(967 982) rotate(-90)">
      <text class="count-text" x="-62" y="12" font-size="30">60</text>
      <text class="words-text" x="-24" y="2" font-size="12.5">MICA POWDER</text>
      <text class="words-text" x="-24" y="13" font-size="9.5">COLORS</text>
    </g>

    <!-- front panel -->
    <g clip-path="url(#clip-front)">
      <rect x="295" y="666" width="601" height="400" fill="url(#wood-grain)" role="img" aria-label="Dark wood texture background"/>
      <rect x="295" y="666" width="290" height="400" fill="var(--ink)"/>
      <ellipse cx="440" cy="880" rx="170" ry="200" fill="url(#powder-burst)" role="img" aria-label="Photograph of a colourful mica powder explosion"/>
      <ellipse cx="862" cy="948" rx="36" ry="28" fill="#2fb7a6" role="img" aria-label="Photograph of a jar of turquoise mica powder"/>
      <ellipse cx="822" cy="1022" rx="55" ry="46" fill="url(#jar-tones)" role="img" aria-label="Photograph of a jar of copper mica powder"/>
    </g>
    <text class="brand-text on-dark" x="727" y="735" font-size="30" text-anchor="middle">Lumen</text>
    <text class="brand-text on-dark" x="727" y="782" font-size="30" text-anchor="middle">Crafts</text>
    <text class="tagline-text" x="724" y="807" text-anchor="middle">60 Vibrant Colors I Multi-Purpose I Cosmetic Grade I Non-Toxic</text>
    <path d="M668 850 Q700 850 710 838 Q724 832 738 838 Q748 850 780 850 Q808 850 808 875 V935 Q808 955 780 955 Q748 955 738 965 Q724 972 710 965 Q700 955 668 955 Q640 955 640 935 V875 Q640 850 668 850 Z" fill="#1b1b1b" stroke="url(#badge-rim)" stroke-width="3"/>
    <text class="badge-count" x="724" y="890" text-anchor="middle">60</text>
    <text class="badge-line" x="724" y="908" text-anchor="middle">INSPIRING</text>
    <text class="badge-line" x="724" y="925" text-anchor="middle">MICA POWDER</text>
    <text class="badge-colors" x="724" y="941" text-anchor="middle">COLORS</text>
    <rect x="584" y="995" width="279" height="21" fill="url(#band-fill)"/>
    <text class="band-text" x="723" y="1009" text-anchor="middle">60 X 5g (0.18 Oz) &#160;|&#160; Includes 3 Measuring Spoons</text>
  </svg>

  <div class="panel-label back-title">BACK</div>
  <div class="panel-label back-note">I can also update tomorrow<br>Complete both Designs<br>Files &amp; 3d Mockup</div>
</main>
</body>
</html>
```